Outdoor mass notification company needing business card design.

Our company name is Harborline Signal Systems Inc located in Amory Mississippi and we sell and maintain "Corvath" Mass Notification Sirens in the US. Outdoor sirens notify people of certain severe dangers such as tornados, severe thunderstorms, flooding, hurricanes and tsunamis. We also serve the oil and gas refining industries to warn of Chemical releases, fires, and lightning alerts.

Contact Information for Business Card

Name, title, cell number, email address

Requirements
Nice to have
• The Corvath logo and also the Tallbrook logo.

```html
<!DOCTYPE html>
<html lang="en">
<head>
<meta charset="utf-8">
<title>Harborline Signal Systems — Business Card</title>
<link rel="stylesheet" href="https://fonts.googleapis.com/css2?family=PT+Serif:wght@700&family=Montserrat:wght@400;700&display=swap">
<style>
  :root {
    --backdrop: #262626;
    --card-white: #f7f7f7;
    --brand-blue: #3b5873;
    --logo-blue: #2f4b67;
    --swoosh-grey: #8c8c8c;
    --siren-dark: #2b2b2b;
    --siren-light: #6a6a6a;
    --text-light: #ffffff;
  }
  * { margin: 0; padding: 0; box-sizing: border-box; }
  html, body { width: 1200px; height: 1059px; overflow: hidden; }
  body { background: var(--backdrop); position: relative; font-family: "Montserrat", sans-serif; }

  .card {
    position: absolute;
    width: 690px;
    height: 392px;
    border-radius: 16px;
    overflow: hidden;
  }
  .card--front { left: 256px; top: 89px; background: var(--card-white); }
  .card--back  { left: 255px; top: 547px; background: var(--brand-blue); }

  .wave { position: absolute; inset: 0; width: 100%; height: 100%; }

  .brand-name {
    font-family: "PT Serif", serif;
    font-weight: 700;
    text-transform: uppercase;
    line-height: 1;
  }
  .card--front .brand-name {
    position: absolute;
    right: 38px;
    top: 64px;
    text-align: right;
    color: var(--logo-blue);
  }
  .card--front .brand-name .line-1 { display: block; font-size: 34px; }
  .card--front .brand-name .line-2 { display: block; font-size: 24px; margin-top: 6px; }

  .siren-photo {
    position: absolute;
    left: 512px;
    top: 168px;
    width: 74px;
    height: 224px;
    background: linear-gradient(180deg, var(--siren-dark) 0%, var(--siren-light) 45%, var(--siren-dark) 100%);
    border-radius: 4px 4px 0 0;
  }

  .contact { position: absolute; left: 33px; top: 218px; color: var(--text-light); }
  .contact .person-name { font-family: "PT Serif", serif; font-weight: 700; font-size: 23px; letter-spacing: 0.3px; }
  .contact .person-title { font-size: 15px; margin-top: 2px; }
  .contact .divider { width: 16px; height: 1px; background: var(--text-light); margin: 14px 0 14px; }
  .contact ul { list-style: none; }
  .contact li { display: flex; align-items: center; gap: 8px; font-size: 15px; height: 27px; }
  .contact li svg { width: 12px; height: 12px; fill: var(--text-light); }

  .card--back .brand-name {
    position: absolute;
    left: 0; right: 0;
    top: 100px;
    text-align: center;
    color: var(--text-light);
  }
  .card--back .brand-name .line-1 { display: block; font-size: 50px; }
  .card--back .brand-name .line-2 { display: block; font-size: 40px; margin-top: 6px; }

  .services { position: absolute; left: 0; right: 0; top: 268px; text-align: center; color: var(--text-light); }
  .services h2 { font-size: 18px; font-weight: 700; letter-spacing: 0.5px; margin-bottom: 14px; }
  .services p { font-size: 17px; line-height: 30px; }
  .services .sep { display: inline-block; margin: 0 9px; font-size: 12px; vertical-align: 2px; }
</style>
</head>
<body>

<section class="card card--front">
  <svg class="wave" viewBox="0 0 690 392" aria-hidden="true">
    <path d="M48 166 C150 118 260 130 360 190 C440 240 520 300 640 282 C520 296 440 256 360 206 C260 146 150 138 48 166Z" fill="var(--swoosh-grey)"/>
    <path d="M0 178 C90 140 210 138 320 196 C420 250 490 308 580 296 C630 288 665 272 690 260 L690 392 L0 392Z" fill="var(--brand-blue)"/>
  </svg>

  <div class="brand-name">
    <span class="line-1">Harborline</span>
    <span class="line-2">Signal Systems</span>
  </div>

  <div class="siren-photo" role="img" aria-label="Photo of a stacked outdoor warning siren on a pole"></div>

  <div class="contact">
    <p class="person-name">DANA WHITFIELD</p>
    <p class="person-title">CEO/Founder</p>
    <div class="divider"></div>
    <ul>
      <li><svg viewBox="0 0 12 12"><path d="M2 1h2l1 3-1.5 1a6 6 0 0 0 3.5 3.5L8 7l3 1v2a1 1 0 0 1-1 1A9 9 0 0 1 1 2a1 1 0 0 1 1-1z"/></svg>(555)014-2273</li>
      <li><svg viewBox="0 0 12 12"><path d="M1 3h10v7H1zM1 3l5 4 5-4" fill="none" stroke="#fff" stroke-width="1.2"/></svg>info@harborlinesignal.com</li>
      <li><svg viewBox="0 0 12 12"><circle cx="6" cy="6" r="5" fill="none" stroke="#fff" stroke-width="1.2"/><path d="M1 6h10M6 1c-2 3-2 7 0 10M6 1c2 3 2 7 0 10" fill="none" stroke="#fff" stroke-width="0.9"/></svg>www.harborlinesignal.com</li>
    </ul>
  </div>
</section>

<section class="card card--back">
  <div class="brand-name">
    <span class="line-1">Harborline</span>
    <span class="line-2">Signal Systems</span>
  </div>

  <div class="services">
    <h2>OUR SERVICES</h2>
    <p>Tornados<span class="sep">|</span>Severe Thunderstorms<span class="sep">|</span>Hurricanes &amp; Tsunamis</p>
    <p>Flooding<span class="sep">|</span>Chemical Releases<span class="sep">|</span>Fires &amp; Lightning Alerts</p>
  </div>
</section>

</body>
</html>
```